Letterhead Design Project

Looking for letterhead designs for Brastova Mining.

I am looking for a letterhead design in conjunction with a business card design. I have opened contests for both but ask that if you submit a letterhead design you also submit a business card design with a corresponding look/feel.

Brastova Mining is a B2B company that buys and sells large machinery tires within the coal mining industry. The design should the strong, crisp and masculine. I have uploaded the company logo and mock-up of the back of the company's business card.

Color scheme should be grey/green/black

Contact information to include:
Name: Dale Whitford
Title: Managing Director
Phone: 555-231-4097
Address: 1817 Pellam #3 Dallas, TX 75290
Email: Dale@Brastova.example
Updates

Project Deadline Extended
Reason: Looking for a more refined, elegant letterhead than what's been submitted as of yet. Here is a sample of what we're looking for: http://www.plumcrestgallery.example/letterhead-designs/ We will also be increasing the payment.

Industry/Entity Type

Coal Mining

```html
<!DOCTYPE html>
<html lang="en">
<head>
<meta charset="utf-8">
<title>Brastova Mining — Letterhead &amp; Business Card</title>
<link rel="stylesheet" href="https://fonts.googleapis.com/css2?family=Roboto+Slab:wght@400;700&family=Roboto:ital,wght@1,400&display=swap">
<style>
  :root {
    --bg: #e4e5e3;
    --paper: #ffffff;
    --black: #0b0b0b;
    --charcoal: #2a2a2a;
    --grey: #8a8a8a;
    --grey-light: #b9b9b9;
    --green: #3f9b2f;
    --green-dark: #1f6a1c;
    --green-light: #8fd14f;
    --white: #ffffff;
    --ink: #2b2b2b;
  }
  * { margin: 0; padding: 0; box-sizing: border-box; }
  html, body { width: 848px; height: 1200px; overflow: hidden; }
  body {
    position: relative;
    background: var(--bg);
    font-family: "Roboto Slab", serif;
    color: var(--ink);
  }

  /* Letterhead */
  .letterhead {
    position: absolute;
    left: 97px; top: 71px;
    width: 547px; height: 777px;
    background: var(--paper);
    box-shadow: 0 4px 14px rgba(0,0,0,.25);
    overflow: hidden;
  }
  .letterhead__header { position: absolute; left: 0; top: 0; width: 547px; height: 103px; }
  .letterhead__header svg, .letterhead__footer-swoosh { position: absolute; left: 0; top: 0; display: block; }
  .brand {
    position: absolute;
    display: flex; align-items: center; gap: 8px;
    color: var(--white);
    font-weight: 700;
    letter-spacing: .04em;
    white-space: nowrap;
  }
  .brand__mark { width: 14px; height: 14px; background: var(--green-light); }
  .letterhead .brand { left: 34px; top: 40px; font-size: 17px; }
  .letterhead__sender {
    position: absolute; right: 22px; top: 40px;
    text-align: right; color: var(--white);
  }
  .sender__name { font-weight: 700; font-size: 11px; }
  .sender__title { font-family: "Roboto", sans-serif; font-style: italic; font-size: 7px; }

  .letterhead__footer-swoosh { top: auto; bottom: 0; }
  .letterhead__contact {
    position: absolute; left: 186px; top: 726px;
    font-size: 9.5px; line-height: 1;
  }
  .contact__row { display: flex; align-items: center; }
  .contact__divider { width: 1px; height: 13px; background: var(--ink); margin: 0 14px 0 20px; }
  .contact__email { margin: 10px 0 0 102px; }

  /* Business card */
  .business-card {
    position: absolute;
    left: 442px; top: 834px;
    width: 392px; height: 249px;
    box-shadow: 0 4px 14px rgba(0,0,0,.35);
    overflow: hidden;
  }
  .business-card svg { position: absolute; left: 0; top: 0; display: block; }
  .business-card .brand { left: 42px; top: 113px; font-size: 15px; }
  .card__sender { position: absolute; right: 14px; top: 18px; text-align: right; color: var(--white); }
  .card__sender .sender__name { font-size: 16px; }
  .card__sender .sender__title { font-size: 10px; }
  .card__contact {
    position: absolute; right: 14px; bottom: 14px;
    text-align: right; color: var(--white);
    font-weight: 700; font-size: 10px; line-height: 1.35;
  }
</style>
</head>
<body>

<section class="letterhead" aria-label="Letterhead">
  <div class="letterhead__header">
    <svg width="547" height="103" viewBox="0 0 547 103">
      <defs>
        <linearGradient id="head-dark" x1="0" y1="0" x2="1" y2="0">
          <stop offset="0" stop-color="#050505"/>
          <stop offset=".55" stop-color="#5a5a5a"/>
          <stop offset="1" stop-color="#8c8c8c"/>
        </linearGradient>
        <linearGradient id="head-green" x1="0" y1="0" x2="1" y2="0">
          <stop offset="0" stop-color="#1f6a1c"/>
          <stop offset="1" stop-color="#4aa935"/>
        </linearGradient>
      </defs>
      <rect width="547" height="103" fill="url(#head-dark)"/>
      <path d="M300 0 C360 10 380 60 460 80 C500 90 530 90 547 88 L547 0 Z" fill="url(#head-green)"/>
      <path d="M250 0 C330 20 350 75 470 92 C505 97 530 96 547 94" fill="none" stroke="#8fd14f" stroke-width="3"/>
      <path d="M230 8 C330 40 360 90 480 100" fill="none" stroke="#c9c9c9" stroke-width="2" opacity=".7"/>
    </svg>
    <div class="brand"><span class="brand__mark"></span>BRASTOVA MINING</div>
    <div class="letterhead__sender">
      <div class="sender__name">Dale Whitford</div>
      <div class="sender__title">Managing Director</div>
    </div>
  </div>

  <svg class="letterhead__footer-swoosh" width="547" height="70" viewBox="0 0 547 70">
    <path d="M0 0 C40 25 90 50 170 70 L0 70 Z" fill="#3f9b2f"/>
    <path d="M0 14 C50 40 110 60 175 70" fill="none" stroke="#8fd14f" stroke-width="4"/>
    <path d="M0 26 C60 50 130 64 180 70" fill="none" stroke="#1a1a1a" stroke-width="5"/>
    <path d="M0 38 C60 58 120 66 150 70 L0 70 Z" fill="#2e7d24"/>
  </svg>

  <div class="letterhead__contact">
    <div class="contact__row">
      <span>Address: 1817 Pellam #3 Dallas, TX 75290</span>
      <span class="contact__divider"></span>
      <span>Phone: 555-231-4097</span>
    </div>
    <div class="contact__email">Email: Dale@Brastova.example</div>
  </div>
</section>

<section class="business-card" aria-label="Business card">
  <svg width="392" height="249" viewBox="0 0 392 249">
    <defs>
      <linearGradient id="card-dark" x1="0" y1="0" x2="1" y2="1">
        <stop offset="0" stop-color="#050505"/>
        <stop offset=".6" stop-color="#3a3a3a"/>
        <stop offset="1" stop-color="#9a9a9a"/>
      </linearGradient>
      <linearGradient id="card-green" x1="0" y1="0" x2="1" y2="1">
        <stop offset="0" stop-color="#4aa935"/>
        <stop offset="1" stop-color="#1f6a1c"/>
      </linearGradient>
    </defs>
    <rect width="392" height="249" fill="url(#card-dark)"/>
    <path d="M171 0 L392 0 L392 249 L171 249 L266 142 Q272 124 266 108 Z" fill="url(#card-green)"/>
    <path d="M171 0 L266 108 Q272 124 266 142 L171 249" fill="none" stroke="#8fd14f" stroke-width="4"/>
  </svg>
  <div class="brand"><span class="brand__mark"></span>BRASTOVA MINING</div>
  <div class="card__sender">
    <div class="sender__name">Dale Whitford</div>
    <div class="sender__title">Managing Director</div>
  </div>
  <div class="card__contact">
    <div>555-231-4097</div>
    <div>Dale@Brastova.example</div>
    <div>1817 Pellam #3 Dallas, TX 75290</div>
  </div>
</section>

</body>
</html>
```